New Innovative Counselling and psychotherapy Service needs Business Card design

Keep it simple and professional. On one side, just company name and logo (perhaps in all blue) and maybe a tag line.

On other side (all white) my name and Qualifications in centre

Industry/Entity Type

Health And Wellness

Contact Information for Business Card

Derek Hollis
Counsellor & Psychotherapist
BSc (Psychol.), BA, Dip. (Couns. & Psych.), PG.Cert (CBT), ADLnR, ESGW

I will also require Mobile no, Email and web site address of which I'll pass on to final designer.

Font styles to use
Sans Serif

Requirements
Must have
• My Logo Only and please use the colours in logo that is in it.
Should not have
• Any other images

```html
<!DOCTYPE html>
<html lang="en">
<head>
<meta charset="utf-8">
<title>Thrive Lane – Business Card</title>
<link rel="stylesheet" href="https://fonts.googleapis.com/css2?family=Source+Sans+3:ital,wght@0,400;0,600;0,700;1,400&display=swap">
<style>
  :root {
    --backdrop: #6e6e6e;
    --brand-blue: #45b3ec;
    --brand-green: #99d45e;
    --card-white: #ffffff;
    --ink-dark: #333333;
    --ink-mid: #555555;
    --text-on-blue: #ffffff;
  }
  * { margin: 0; padding: 0; box-sizing: border-box; }
  html, body {
    width: 1200px;
    height: 802px;
    overflow: hidden;
    background: var(--backdrop);
    font-family: "Source Sans 3", sans-serif;
  }
  .canvas {
    position: relative;
    width: 1200px;
    height: 802px;
  }
  .card {
    position: absolute;
    top: 274px;
    width: 443px;
    height: 265px;
  }
  .card--front {
    left: 136px;
    background: var(--brand-blue);
    color: var(--text-on-blue);
  }
  .card--back {
    left: 624px;
    background: var(--card-white);
  }
  .contact-block {
    position: absolute;
    right: 26px;
    top: 48px;
    text-align: right;
  }
  .holder-name {
    font-size: 19px;
    font-weight: 600;
    line-height: 1.05;
    letter-spacing: -0.2px;
  }
  .holder-role {
    font-size: 12.5px;
    font-weight: 700;
    line-height: 1.25;
  }
  .holder-quals {
    font-size: 12px;
    font-style: italic;
    line-height: 1.3;
    margin-top: 2px;
  }
  .contact-list {
    position: absolute;
    right: 26px;
    top: 178px;
    list-style: none;
    text-align: right;
    font-size: 12px;
    line-height: 16px;
  }
  .contact-list li {
    display: flex;
    justify-content: flex-end;
    align-items: center;
    gap: 3px;
  }
  .contact-icon {
    width: 10px;
    height: 10px;
    fill: var(--text-on-blue);
  }
  .brand-lockup {
    position: absolute;
    left: 97px;
    top: 106px;
    display: flex;
    align-items: center;
    gap: 18px;
  }
  .brand-dot {
    width: 48px;
    height: 48px;
    border-radius: 50%;
    background: var(--brand-blue);
  }
  .brand-name {
    font-size: 27px;
    font-weight: 400;
    color: var(--ink-dark);
    letter-spacing: -0.2px;
  }
  .tagline {
    position: absolute;
    left: 0;
    right: 0;
    top: 201px;
    padding-left: 88px;
    font-size: 16px;
    font-weight: 600;
    color: var(--ink-mid);
    text-align: center;
    letter-spacing: -0.2px;
  }
</style>
</head>
<body>
<main class="canvas">

  <section class="card card--front" aria-label="Business card, contact side">
    <div class="contact-block">
      <h1 class="holder-name">DEREK HOLLIS</h1>
      <p class="holder-role">Counsellor &amp; Psychotherapist</p>
      <p class="holder-quals">BSc (Psychol.), BA<br>Dip. (Couns. &amp; Psych.),<br>PG.Cert (CBT), ADLnR, ESGW</p>
    </div>
    <ul class="contact-list">
      <li>086 5521 907
        <svg class="contact-icon" viewBox="0 0 10 10" aria-hidden="true"><path d="M1 3.2C1 2 2.2 1.5 5 1.5S9 2 9 3.2V4H7V3.2H3V4H1z M2.5 4.5h5L8.5 8.5h-7z"/></svg>
      </li>
      <li>info@thrivelane.com
        <svg class="contact-icon" viewBox="0 0 10 10" aria-hidden="true"><path d="M0.5 2h9v6h-9z M1.2 2.6L5 5.5 8.8 2.6" stroke="#45b3ec" stroke-width="0.7"/></svg>
      </li>
      <li>www.thrivelane.com
        <svg class="contact-icon" viewBox="0 0 10 10" aria-hidden="true"><circle cx="5" cy="5" r="4.5"/><path d="M3 3.5l2 -1 1 1.5-1.5 1 1 2.5-2-1z" fill="#45b3ec"/></svg>
      </li>
    </ul>
  </section>

  <section class="card card--back" aria-label="Business card, brand side">
    <div class="brand-lockup">
      <span class="brand-dot" aria-hidden="true"></span>
      <span class="brand-name">Thrive Lane</span>
    </div>
    <p class="tagline">caring for your &nbsp;psychological well-being</p>
  </section>

</main>
</body>
</html>
```